COMPANY NAME ------ Velmora22 Brands, Inc. TAGLINE......... Simply Velmora!

I need Graphic design for Coconut oil Skincare products!
I need a graphic design that portrays LUXURY AS APPLIED TO MY COMPANY AND THE TAGLINE ! UPSCALE!!
COLOR LAYOUT ................. GOLD ON BLACK, GOLD ON CHOCOLATE LIKE COLOR!
The designers can focus their graphic design based more the word.." "LUXURY"..... The logo I submitted is the two logo I picked.. the logo and the slogan has to be incorporated in the graphic design... The label has to be "ELEGANT" and " UPSCALE".. It can also be "BOLD".

Target Market(s)

20 - 45 years

Industry/Entity Type

Graphic Design

Font styles to use
Decorative

Requirements
Must have
• Luxury feel to it....
Nice to have
• Logo on the label and oil pouring from inside Coconuts !
Should not have
• Local or Country feel because of the word Coconut oil

```html
<!DOCTYPE html>
<html lang="en">
<head>
<meta charset="utf-8">
<title>BelaBela Coconut Oil Label</title>
<link rel="stylesheet" href="https://fonts.googleapis.com/css2?family=Great+Vibes&family=Josefin+Sans:wght@300;400&family=Questrial&family=Nunito:wght@700&display=swap">
<style>
  :root {
    --paper: #ffffff;
    --chocolate: #3b170a;
    --chocolate-light: #46200f;
    --flourish: #5a3223;
    --gold: #b8962e;
    --gold-deep: #8a6a1c;
    --gold-bright: #c9a335;
    --cream: #fbf4e2;
  }
  html, body {
    margin: 0;
    padding: 0;
    width: 1200px;
    height: 2247px;
    overflow: hidden;
    background: var(--paper);
  }
  .label {
    position: absolute;
    left: 125px;
    top: 102px;
    width: 952px;
    height: 2046px;
    border-radius: 28px;
    background: var(--chocolate);
    overflow: hidden;
  }
  .brand-mark {
    position: absolute;
    left: 50%;
    top: 150px;
    width: 250px;
    height: 250px;
    margin-left: -125px;
    border-radius: 50%;
    background: var(--gold-deep);
  }
  .brand-name {
    position: absolute;
    left: 0;
    width: 100%;
    top: 480px;
    text-align: center;
    font-family: "Questrial", sans-serif;
    font-size: 70px;
    line-height: 1;
    color: var(--gold-deep);
    letter-spacing: 1px;
  }
  .brand-tagline {
    position: absolute;
    left: 0;
    width: 100%;
    top: 585px;
    text-align: center;
    font-family: "Nunito", sans-serif;
    font-weight: 700;
    font-size: 30px;
    line-height: 1;
    color: var(--gold-bright);
    letter-spacing: 1px;
  }
  .product-name {
    position: absolute;
    left: 0;
    width: 100%;
    top: 760px;
    text-align: center;
    font-family: "Great Vibes", cursive;
    font-size: 190px;
    line-height: 1.2;
    color: var(--gold);
  }
  .product-type {
    position: absolute;
    left: 0;
    width: 100%;
    top: 1002px;
    text-align: center;
    font-family: "Josefin Sans", sans-serif;
    font-weight: 400;
    font-size: 78px;
    line-height: 1.12;
    color: var(--gold);
    letter-spacing: 15px;
    text-indent: 15px;
  }
  .flourish-band {
    position: absolute;
    left: 0;
    top: 1293px;
    width: 100%;
    height: 408px;
    background: linear-gradient(90deg, var(--chocolate-light), var(--flourish) 50%, var(--chocolate-light));
    opacity: 0.55;
  }
  .volume-badge {
    position: absolute;
    left: 322px;
    top: 1738px;
    width: 308px;
    height: 320px;
  }
  .volume-text {
    position: absolute;
    left: 322px;
    top: 1845px;
    width: 308px;
    text-align: center;
    font-family: "Josefin Sans", sans-serif;
    font-weight: 300;
    font-size: 46px;
    line-height: 72px;
    color: var(--cream);
  }
</style>
</head>
<body>
  <main class="label">
    <div class="brand-mark" aria-hidden="true"></div>
    <div class="brand-name">Velmora22</div>
    <div class="brand-tagline">Simply Velmora!</div>

    <h1 class="product-name" style="margin:0;font-weight:400;">BelaBela</h1>
    <div class="product-type">COCONUT<br>OIL</div>

    <div class="flourish-band" role="img" aria-label="Band of fine swirling floral scrollwork in soft brown lines"></div>

    <svg class="volume-badge" viewBox="0 0 308 320" aria-hidden="true">
      <path d="M2 320 V154 A152 152 0 0 1 306 154 V320" fill="none" stroke="var(--gold)" stroke-width="4"/>
      <path d="M14 320 V154 A140 140 0 0 1 294 154 V320 Z" fill="var(--gold)"/>
    </svg>
    <div class="volume-text">14 FL OZ<br>(414mL)</div>
  </main>
</body>
</html>
```